Icon Design Project - Icon Set with 6 Icons

For our web site and product line, we need 6 icons.

Each icon targets
1) REUNION
2) GROUP EVENT FUNDRAISER
3) GROUP & SPORTS EVENT
4) CORPORATE EVENT
5) PERSONAL FUNDRAISER
6) PERSONAL EVENT

-Please see logo attached. Each icon should use the color from the logo alone (6 colors), or may be with one other color (white, black)

-Here below are example of potential icons per category. You can use those ideas or create your own to reflect the target market.

-Please make sure not to use the same icon twice.

-We want them to look very sharp and simple:

1) REUNION – possible icons
-Bunch of people talking together
-Graduation hat
-Ballons

2) GROUP EVENT FUNDRAISER - possible icons
-Thermometer
-Group plus thermometer (since a group fundraiser)

3) GROUP & SPORTS EVENT – possible icons
-Icon with sports
-Icon with golf ball or golf club
-Etc.

4) CORPORATE EVENT – possible Icons
-Profit chart
-Building
-Badge to a show

5) PERSONAL FUNDRAISER - possible icons
-A hand (helping out)
-Thermometer

6) PERSONAL EVENT – possible icons
-Calendar
-Ballon(s)
-Graffity
-Invitation

Current site www.GalaNook.net will be updated. Simulation of the site where the icons will be also attached.

Industry/Entity Type

Club

Requirements
Must have
• Needs to be powerful yet SIMPLE.

Use one color from the logo (attached) to represent each icon. Could be one color only, or may be with another like black or white.

```html
<!DOCTYPE html>
<html lang="en">
<head>
<meta charset="utf-8">
<title>GalaNook – Event Categories</title>
<link href="https://fonts.googleapis.com/css2?family=Open+Sans:wght@400;600;700&display=swap" rel="stylesheet">
<style>
  :root {
    --header-bg: #262626;
    --header-rule: #8a8a8a;
    --accent-orange: #f07f1e;
    --white: #ffffff;
    --ink: #141414;
    --page-bg: #ffffff;
    --reunion: #b3245c;
    --group-fund: #6db33a;
    --sports: #e7801d;
    --corporate: #1d8ecf;
    --personal-fund: #129944;
    --personal-event: #efb219;
  }
  * { margin: 0; padding: 0; box-sizing: border-box; }
  html, body { width: 1200px; height: 1000px; overflow: hidden; background: var(--page-bg); }
  body { font-family: "Open Sans", Arial, sans-serif; position: relative; }

  .site-header { position: absolute; left: 0; top: 0; width: 1200px; height: 90px; background: var(--header-bg); border-bottom: 2px solid var(--header-rule); }
  .brand { position: absolute; left: 26px; top: 30px; display: flex; align-items: center; gap: 14px; }
  .brand-dot { width: 60px; height: 52px; border-radius: 50%; background: var(--white); }
  .brand-name { color: var(--white); font-size: 40px; font-weight: 600; line-height: 1; letter-spacing: -0.5px; }

  .utility { position: absolute; top: 8px; right: 18px; display: flex; align-items: center; height: 26px; font-size: 16px; font-weight: 700; }
  .utility .tenure { color: var(--accent-orange); font-weight: 600; padding-right: 14px; }
  .utility .phone { color: var(--white); padding: 0 12px 0 10px; border-left: 1px solid #bbb; height: 26px; display: flex; align-items: center; }
  .utility .login { color: var(--white); padding-left: 10px; border-left: 1px solid #bbb; height: 26px; display: flex; align-items: center; }

  .main-nav { position: absolute; top: 61px; left: 0; width: 1200px; font-size: 13px; font-weight: 700; color: var(--white); }
  .main-nav span { position: absolute; }
  .trial-btn { position: absolute; left: 1080px; top: 51px; width: 107px; height: 28px; border-radius: 5px; background: var(--accent-orange); color: var(--white); font-size: 14px; font-weight: 700; display: flex; align-items: center; justify-content: center; }

  .hero { position: absolute; left: 0; top: 90px; width: 1200px; height: 480px;
    background:
      linear-gradient(180deg, rgba(150,140,220,0.9) 0%, rgba(110,90,190,0.85) 25%, rgba(190,170,220,0.7) 45%, rgba(60,50,90,0.9) 70%, #1e1a2a 100%); }

  .categories { position: absolute; top: 618px; left: 0; width: 1200px; }
  .category { position: absolute; width: 160px; text-align: center; }
  .badge { width: 100px; height: 100px; margin: 0 auto; border-radius: 50%; background: #f3f3f3; box-shadow: 0 10px 12px -6px rgba(0,0,0,0.18), inset 0 0 0 1px #ddd; display: flex; align-items: center; justify-content: center; }
  .badge svg { width: 88px; height: 88px; }
  .label { margin-top: 8px; font-size: 20px; line-height: 27px; color: var(--ink); }
</style>
</head>
<body>
  <header class="site-header">
    <div class="brand"><span class="brand-dot"></span><span class="brand-name">galanook</span></div>
    <div class="utility">
      <span class="tenure">11 years online</span>
      <span class="phone">1-800-555-0142</span>
      <span class="login">LOGIN</span>
    </div>
    <nav class="main-nav">
      <span style="left:434px;top:3px">XXXXXXX</span>
      <span style="left:541px;top:1px">XXXXXXX</span>
      <span style="left:640px;top:0">XXXXXXX</span>
      <span style="left:748px;top:-3px">XXXXXXX</span>
      <span style="left:841px;top:0">XXXXXXX</span>
      <span style="left:948px;top:-3px">XXXXXXX</span>
    </nav>
    <div class="trial-btn">FREE TRIAL</div>
  </header>

  <div class="hero" role="img" aria-label="Photo of a gala event in a draped tent with chandeliers and a seated audience"></div>

  <section class="categories">
    <div class="category" style="left:122px">
      <div class="badge"><svg viewBox="0 0 88 88">
        <defs><radialGradient id="gReunion" cx="40%" cy="30%" r="70%"><stop offset="0" stop-color="#e2588e"/><stop offset="1" stop-color="var(--reunion)"/></radialGradient></defs>
        <circle cx="44" cy="44" r="44" fill="url(#gReunion)"/>
        <path d="M14 38 L44 26 L74 38 L44 50 Z" fill="none" stroke="#fff" stroke-width="3" stroke-linejoin="round"/>
        <path d="M26 44 V58 C34 64 54 64 62 58 V44" fill="none" stroke="#fff" stroke-width="3"/>
        <path d="M66 41 V60" stroke="#fff" stroke-width="2.5"/><path d="M63 60 h6 l-1 9 h-4z" fill="#fff"/>
      </svg></div>
      <div class="label">reunion</div>
    </div>

    <div class="category" style="left:277px">
      <div class="badge"><svg viewBox="0 0 88 88">
        <defs><radialGradient id="gGroupFund" cx="40%" cy="30%" r="70%"><stop offset="0" stop-color="#a6d96e"/><stop offset="1" stop-color="var(--group-fund)"/></radialGradient></defs>
        <circle cx="44" cy="44" r="44" fill="url(#gGroupFund)"/>
        <path d="M38 16 a6 6 0 0 1 12 0 V56 a11 11 0 1 1 -12 0 Z" fill="none" stroke="#fff" stroke-width="3"/>
        <rect x="42" y="34" width="4" height="28" fill="#fff"/><circle cx="44" cy="65" r="6" fill="#fff"/>
        <path d="M52 22h5M52 30h5M52 38h5M52 46h5" stroke="#fff" stroke-width="2"/>
      </svg></div>
      <div class="label">group event<br>fundraiser</div>
    </div>

    <div class="category" style="left:432px">
      <div class="badge"><svg viewBox="0 0 88 88">
        <defs><radialGradient id="gSports" cx="40%" cy="30%" r="70%"><stop offset="0" stop-color="#f6b04a"/><stop offset="1" stop-color="var(--sports)"/></radialGradient></defs>
        <circle cx="44" cy="44" r="44" fill="url(#gSports)"/>
        <path d="M58 14 L38 64" stroke="#fff" stroke-width="3.5" stroke-linecap="round"/>
        <path d="M38 64 L26 66 L28 72 L42 68 Z" fill="#fff"/>
        <circle cx="58" cy="66" r="6" fill="none" stroke="#fff" stroke-width="2.5"/>
        <path d="M66 26 C74 38 74 54 66 64" fill="none" stroke="#fff" stroke-width="2.5"/>
      </svg></div>
      <div class="label">group &amp; sports<br>event</div>
    </div>

    <div class="category" style="left:582px">
      <div class="badge"><svg viewBox="0 0 88 88">
        <defs><radialGradient id="gCorp" cx="40%" cy="30%" r="70%"><stop offset="0" stop-color="#5cc0ee"/><stop offset="1" stop-color="var(--corporate)"/></radialGradient></defs>
        <circle cx="44" cy="44" r="44" fill="url(#gCorp)"/>
        <g fill="none" stroke="#fff" stroke-width="2.5">
          <rect x="22" y="52" width="8" height="18"/><rect x="34" y="46" width="8" height="24"/>
          <rect x="46" y="40" width="8" height="30"/><rect x="58" y="32" width="8" height="38"/>
          <path d="M18 46 L40 34 L50 38 L70 22"/>
        </g>
        <path d="M62 18 L74 18 L72 30 Z" fill="#fff"/>
      </svg></div>
      <div class="label">corporate<br>event</div>
    </div>

    <div class="category" style="left:740px">
      <div class="badge"><svg viewBox="0 0 88 88">
        <defs><radialGradient id="gPersFund" cx="40%" cy="30%" r="70%"><stop offset="0" stop-color="#45c06e"/><stop offset="1" stop-color="var(--personal-fund)"/></radialGradient></defs>
        <circle cx="44" cy="44" r="44" fill="url(#gPersFund)"/>
        <path d="M30 72 L26 50 L20 38 C19 34 24 32 26 36 L32 46 L34 22 C34 18 40 18 40 22 L41 38 L44 16 C45 12 51 13 50 17 L48 38 L54 20 C55 16 61 18 60 22 L55 42 L62 30 C64 27 69 29 67 33 L58 58 L52 72 Z" fill="none" stroke="#fff" stroke-width="2.8" stroke-linejoin="round"/>
      </svg></div>
      <div class="label">personal<br>fundraiser</div>
    </div>

    <div class="category" style="left:895px">
      <div class="badge"><svg viewBox="0 0 88 88">
        <defs><radialGradient id="gPersEvent" cx="40%" cy="30%" r="70%"><stop offset="0" stop-color="#fbd562"/><stop offset="1" stop-color="var(--personal-event)"/></radialGradient></defs>
        <circle cx="44" cy="44" r="44" fill="url(#gPersEvent)"/>
        <rect x="18" y="22" width="52" height="46" rx="4" fill="none" stroke="#fff" stroke-width="3"/>
        <path d="M18 32 H70" stroke="#fff" stroke-width="3"/>
        <path d="M30 16 v10 M58 16 v10" stroke="#fff" stroke-width="3.5" stroke-linecap="round"/>
        <g fill="#fff">
          <rect x="25" y="38" width="8" height="6"/><rect x="36" y="38" width="8" height="6"/><rect x="47" y="38" width="8" height="6"/><rect x="58" y="38" width="6" height="6"/>
          <rect x="25" y="48" width="8" height="6"/><rect x="36" y="48" width="8" height="6"/><rect x="47" y="48" width="8" height="6"/><rect x="58" y="48" width="6" height="6"/>
          <rect x="25" y="58" width="8" height="5"/><rect x="36" y="58" width="8" height="5"/>
        </g>
      </svg></div>
      <div class="label">personal<br>event</div>
    </div>
  </section>
</body>
</html>
```